Varnock Travel letterhead design

We need a design for a simple document where we can dump our own information within it. A simple letterhead style. No address or phone details etc are required. More just our logo and free format. Hope this makes sense !

```html
<!DOCTYPE html>
<html lang="en">
<head>
<meta charset="utf-8">
<title>Varnock Travel Letterhead</title>
<link href="https://fonts.googleapis.com/css2?family=Roboto:wght@300;400;500;700&display=swap" rel="stylesheet">
<style>
  :root {
    --backdrop: #e6e6e6;
    --paper: #fcfcfc;
    --navy: #1f3e73;
    --ink: #6f6f6f;
    --ink-strong: #5e5e5e;
    --muted: #b3b3b3;
    --band-grey: #bcbcbc;
    --map-tint: #f4f4f4;
    --sig-tint: #dfe5ef;
  }
  * { margin: 0; padding: 0; box-sizing: border-box; }
  html, body {
    width: 1116px; height: 1200px; overflow: hidden;
    background: var(--backdrop);
    font-family: "Roboto", Arial, sans-serif;
  }
  .letterhead {
    position: absolute; left: 134px; top: 0;
    width: 848px; height: 1200px;
    background: var(--paper);
    color: var(--ink);
  }
  .brand {
    position: absolute; left: 0; right: 0; top: 80px;
    text-align: center;
    font-size: 46px; font-weight: 700; letter-spacing: -1px;
    color: var(--navy);
  }
  .map-backdrop {
    position: absolute; left: 59px; top: 398px;
    width: 755px; height: 435px;
    background: radial-gradient(ellipse at center, var(--map-tint) 0%, rgba(244,244,244,0) 75%);
  }
  .letter {
    position: absolute; left: 87px; top: 250px; width: 709px;
    font-size: 13.5px; line-height: 19.3px;
  }
  .date { margin-bottom: 38px; }
  .recipient { margin-bottom: 38px; }
  .recipient strong { font-weight: 500; color: var(--ink-strong); }
  .greeting { margin-bottom: 19px; }
  .body-copy p { text-align: justify; margin-bottom: 19.3px; }
  .sign-off {
    position: absolute; left: 87px; top: 905px;
    font-size: 13.5px; line-height: 19.3px;
  }
  .sign-off .signer { font-weight: 500; color: var(--ink-strong); }
  .signature {
    width: 180px; height: 38px; margin: 4px 0 6px -16px;
    background: linear-gradient(90deg, var(--sig-tint), rgba(223,229,239,0.3));
    border-radius: 4px;
  }
  .contact {
    position: absolute; left: 0; right: 0; top: 1151px;
    display: flex; justify-content: center; gap: 12px;
    font-size: 15px; font-weight: 300; color: var(--muted);
  }
  .contact span { display: inline-flex; align-items: center; gap: 8px; }
  .contact svg { width: 14px; height: 14px; }
  .footer-band {
    position: absolute; top: 1188px; left: 207px;
    width: 434px; height: 12px; display: flex;
  }
  .footer-band .grey { flex: 1; background: var(--band-grey); }
  .footer-band .navy { flex: 1; background: var(--navy); }
</style>
</head>
<body>
<main class="letterhead">
  <div class="brand">Varnock Travel</div>

  <div class="map-backdrop" role="img" aria-label="Faint world map watermark"></div>

  <section class="letter">
    <p class="date">30/20/2016</p>
    <address class="recipient" style="font-style:normal">
      <strong>Mr. XYZ Smith</strong><br>
      123, Street No. 123,<br>
      City Name<br>
      Pincode-123456
    </address>
    <p class="greeting">Dear Sir,</p>
    <div class="body-copy">
      <p>Lorem Ipsum is simply dummy text of the printing and typesetting industry. Lorem Ipsum has been the industry's standard dummy text ever since the 1500s, when an unknown printer took a galley of type and scrambled it to make a type specimen book. It has survived not only five centuries, but also the leap into electronic typesetting, remaining essentially unchanged. It was popularised in the 1960s with the release of Linoset sheets containing Lorem Ipsum passages, and more recently with desktop publishing software like Folio PageBuilder including versions of Lorem Ipsum.</p>
      <p>Lorem Ipsum is simply dummy text of the printing and typesetting industry. Lorem Ipsum has been the industry's standard dummy text ever since the 1500s, when an unknown printer took a galley of type and scrambled it to make a type specimen book. It has survived not only five centuries, but also the leap into electronic typesetting, remaining essentially unchanged. It was popularised in the 1960s with the release of Linoset sheets containing Lorem Ipsum passages, and more recently with desktop publishing software like Folio PageBuilder including versions of Lorem Ipsum.</p>
      <p>Lorem Ipsum is simply dummy text of the printing and typesetting industry. Lorem Ipsum has been the industry's standard dummy text ever since the 1500s, when an unknown printer took a galley of type and scrambled it to make a type specimen book.</p>
      <p>Lorem Ipsum is simply dummy text of the printing and typesetting industry. Lorem Ipsum has been the industry's standard dummy text ever since the 1500s, when an unknown printer took a galley of type and scrambled it to make a type specimen book.</p>
    </div>
  </section>

  <section class="sign-off">
    <p class="signer">Your Name</p>
    <div class="signature" role="img" aria-label="Handwritten signature"></div>
    <p class="title">CEO &nbsp;|&nbsp; Owner</p>
  </section>

  <footer>
    <div class="contact">
      <span>
        <svg viewBox="0 0 14 14" fill="none" stroke="#1f3e73" stroke-width="1.2"><rect x="1" y="3" width="12" height="8"/><path d="M1 3l6 5 6-5M1 11l4.5-4M13 11l-4.5-4"/></svg>
        info@VarnockTravel.com
      </span>
      <span>
        <svg viewBox="0 0 14 14" fill="none" stroke="#1f3e73" stroke-width="1.1"><circle cx="7" cy="7" r="6"/><ellipse cx="7" cy="7" rx="2.6" ry="6"/><path d="M1 7h12M2 4h10M2 10h10"/></svg>
        www.VarnockTravel.com
      </span>
    </div>
    <div class="footer-band"><div class="grey"></div><div class="navy"></div></div>
  </footer>
</main>
</body>
</html>
```